I need a business card to give to prospective clients. I am a freelance photographer who photographs most things (except weddings and social stuff) including nature, wildlife and interiors.
I want to look modern and stylish.
I am including a photograph although I am by no means certain that it should be used - what do you think?
More of my images can be seen and downloaded at my Lensora page - just search for Marla Vintree
Target Market(s)
Home owners selling or letting properties, private individuals wanting to buy prints
Industry/Entity Type
Business
Contact Information for Business Card
Marla Vintree Photography
Marla
Fenwick Lodge, Copper Mill Road, Ashbrook, Bury St Edmunds, IP31 4QT
Tel: +44 7700 418263. Email: marla@marlavintree.co.uk

```html
<!DOCTYPE html>
<html lang="en">
<head>
<meta charset="utf-8">
<title>Marla Vintree Photography – Business Card</title>
<link rel="stylesheet" href="https://fonts.googleapis.com/css2?family=Cormorant+Garamond:wght@400;500&family=EB+Garamond:wght@400&display=swap">
<style>
  :root {
    --page-bg: #e4e4e2;
    --card-light: #c9cbc8;
    --card-mid: #8a8f8c;
    --card-dark: #2f3532;
    --ink-light: #f2f3f1;
    --ink-soft: #dfe2df;
    --halftone: rgba(120, 128, 124, 0.55);
    --photo-light: #e6e6e4;
    --photo-dark: #4a4b4a;
  }
  * { margin: 0; padding: 0; box-sizing: border-box; }
  html, body {
    width: 1200px;
    height: 788px;
    overflow: hidden;
    background: var(--page-bg);
  }
  .canvas {
    position: relative;
    width: 1200px;
    height: 788px;
    display: flex;
    align-items: center;
    justify-content: center;
    gap: 40px;
  }
  .card {
    position: relative;
    width: 540px;
    height: 310px;
    overflow: hidden;
    box-shadow: 0 6px 18px rgba(0,0,0,0.18);
  }
  .card--back {
    background: linear-gradient(100deg, var(--card-light) 0%, var(--card-mid) 45%, var(--card-dark) 100%);
  }
  .card--front {
    background: linear-gradient(100deg, var(--card-light) 0%, var(--card-mid) 40%, var(--card-dark) 100%);
  }
  .halftone-field {
    position: absolute;
    background: radial-gradient(ellipse at 70% 55%, var(--halftone) 0%, rgba(120,128,124,0.25) 45%, rgba(120,128,124,0) 72%);
  }
  .card--back .halftone-field { left: 250px; top: -20px; width: 320px; height: 350px; }
  .card--front .halftone-field { left: 150px; top: 80px; width: 420px; height: 260px; }

  .contact-list {
    position: absolute;
    left: 300px;
    top: 118px;
    list-style: none;
    font-family: "EB Garamond", serif;
    font-size: 15px;
    color: var(--ink-light);
    line-height: 1.45;
    white-space: nowrap;
  }
  .contact-item {
    display: flex;
    align-items: center;
    gap: 12px;
    margin-bottom: 14px;
  }
  .contact-icon {
    width: 14px;
    height: 14px;
    flex: none;
    fill: var(--ink-soft);
  }
  .address-line { display: block; }

  .studio-name {
    position: absolute;
    top: 58px;
    left: 0;
    width: 100%;
    text-align: center;
    font-family: "Cormorant Garamond", serif;
    font-weight: 500;
    font-size: 21px;
    letter-spacing: 4px;
    color: var(--ink-light);
    white-space: nowrap;
  }
  .feature-photo {
    position: absolute;
    left: 210px;
    top: 100px;
    width: 124px;
    height: 124px;
    border-radius: 50%;
    background: radial-gradient(circle at 40% 40%, var(--photo-light) 0%, #a9aaa8 45%, var(--photo-dark) 100%);
  }
  .studio-tagline {
    position: absolute;
    top: 258px;
    left: 0;
    width: 100%;
    text-align: center;
    font-family: "Cormorant Garamond", serif;
    font-size: 15px;
    letter-spacing: 22px;
    padding-left: 22px;
    color: var(--ink-light);
    white-space: nowrap;
  }
</style>
</head>
<body>
<main class="canvas">
  <section class="card card--back" aria-label="Business card, back">
    <div class="halftone-field" role="img" aria-label="Halftone dot pattern sweeping across the card"></div>
    <ul class="contact-list">
      <li class="contact-item">
        <svg class="contact-icon" viewBox="0 0 24 24" aria-hidden="true"><path d="M6.6 10.8a15.1 15.1 0 0 0 6.6 6.6l2.2-2.2c.3-.3.7-.4 1-.2 1.1.4 2.3.6 3.6.6.6 0 1 .4 1 1V20c0 .6-.4 1-1 1C10.6 21 3 13.4 3 4c0-.6.4-1 1-1h3.5c.6 0 1 .4 1 1 0 1.3.2 2.5.6 3.6.1.3 0 .7-.2 1z"/></svg>
        <span>+44 7700 418263</span>
      </li>
      <li class="contact-item">
        <svg class="contact-icon" viewBox="0 0 24 24" aria-hidden="true"><path d="M12 2a7 7 0 0 0-7 7c0 5.2 7 13 7 13s7-7.8 7-13a7 7 0 0 0-7-7zm0 9.5A2.5 2.5 0 1 1 12 6.5a2.5 2.5 0 0 1 0 5z"/></svg>
        <span>
          <span class="address-line">Copper Mill Road, Ashbrook</span>
          <span class="address-line">Hollowford, IP31 4QT</span>
        </span>
      </li>
      <li class="contact-item">
        <svg class="contact-icon" viewBox="0 0 24 24" aria-hidden="true"><path d="M3 5h18v14H3zM3 6l9 7 9-7v2l-9 7-9-7z"/></svg>
        <span>marla@marlavintree.co.uk</span>
      </li>
    </ul>
  </section>

  <section class="card card--front" aria-label="Business card, front">
    <div class="halftone-field" role="img" aria-label="Halftone dot pattern sweeping across the card"></div>
    <h1 class="studio-name">MARLA VINTREE</h1>
    <div class="feature-photo" role="img" aria-label="Black and white wildlife photograph in a circular frame"></div>
    <p class="studio-tagline">PHOTOGRAPHY</p>
  </section>
</main>
</body>
</html>
```